Helicopter scenic /Charter company

Need a sign 920mm x 920mm for our Marlow Helipad fence that catches the eye for people walking past. Some photos have been attached but feel free to use helicopter photos you have as well. Like the sign to be black with lettering that stands out. You may do a design with photos or it may look better without. It is up to you. It just has to look eye catching and exciting.
Text: Helicopter Joy Flights & Scenic Tours here seven days from October to March. Prices from just $99 per person* Details at wendaloft.com.au or ph 9372 6105
* $99 flights are shared 8 minute flights and are only available on weekends

Target Market(s)

Tourists locals walking past the helipad

Requirements
Must have
• Logo
• Text as in project description

```html
<!DOCTYPE html>
<html lang="en">
<head>
<meta charset="utf-8">
<title>Wendaloft Helicopters – Joy Flights Sign</title>
<link href="https://fonts.googleapis.com/css2?family=Anton&family=Fira+Sans+Condensed:wght@500;600;700&display=swap" rel="stylesheet">
<style>
  :root {
    --ink: #111111;
    --black: #141414;
    --yellow: #fff200;
    --yellow-soft: #fff98a;
    --blue: #1b6fb5;
    --blue-deep: #1565a8;
    --navy: #1a2540;
    --white: #ffffff;
    --page: #ececec;
  }
  * { box-sizing: border-box; margin: 0; padding: 0; }
  html, body { width: 1200px; height: 1200px; overflow: hidden; background: var(--page); }
  .sign {
    position: absolute; left: 171px; top: 28px;
    width: 858px; height: 1144px;
    background: var(--white);
    box-shadow: 0 4px 18px rgba(0,0,0,.18);
    overflow: hidden;
  }
  .header {
    position: absolute; left: 0; top: 0; width: 100%; height: 366px;
    background: var(--black);
  }
  .headline {
    position: absolute; right: 286px; top: 72px;
    display: flex; flex-direction: column; align-items: flex-end;
    white-space: nowrap;
    font-family: "Anton", sans-serif; line-height: 1;
  }
  .headline .line-one { font-size: 56px; letter-spacing: -0.5px; }
  .headline .line-two { font-size: 86px; margin-top: 12px; letter-spacing: -1px; }
  .headline .season { font-size: 31px; color: var(--white); margin-top: 18px; letter-spacing: -0.5px; }
  .hl-yellow { color: var(--yellow); }
  .hl-blue { color: var(--blue); }
  .price-pennant { position: absolute; left: 594px; top: 0; width: 219px; height: 474px; z-index: 2; }
  .price-pennant text { font-family: "Anton", sans-serif; fill: var(--ink); text-anchor: middle; }
  .photo {
    position: absolute; left: 0; top: 366px; width: 100%; height: 444px;
    background: linear-gradient(115deg, #1e9fb8 0%, #46c0cf 34%, #a9dfdc 48%, #e8dcc2 58%, #d9cfb0 70%, #8c9a66 84%, #6b7d55 100%);
  }
  .offer-band {
    position: absolute; left: 0; top: 810px; width: 100%; height: 140px;
    background: var(--blue-deep);
    font-family: "Fira Sans Condensed", sans-serif; font-weight: 600;
    color: var(--white); font-size: 50px; line-height: 1.15;
    padding: 12px 0 0 42px; letter-spacing: -1px; white-space: nowrap;
  }
  .offer-band .accent { color: var(--yellow); }
  .footer {
    position: absolute; left: 0; top: 950px; width: 100%; height: 194px;
    background: var(--white);
  }
  .brand {
    position: absolute; left: 42px; top: 46px;
    display: flex; align-items: center; gap: 16px;
  }
  .brand-dot { width: 64px; height: 64px; border-radius: 50%; background: var(--blue); }
  .brand-name {
    font-family: "Fira Sans Condensed", sans-serif; font-weight: 700;
    color: var(--navy); font-size: 42px; line-height: 1.05; letter-spacing: -0.5px;
  }
  .contact {
    position: absolute; right: 50px; top: 22px;
    font-family: "Fira Sans Condensed", sans-serif; font-weight: 600;
    color: var(--ink); font-size: 34px; letter-spacing: -0.5px; white-space: nowrap;
  }
  .contact .row { display: flex; align-items: center; gap: 12px; margin-top: 10px; }
  .contact .row.web { font-size: 30px; margin-top: 16px; }
  .contact .icon { width: 28px; height: 28px; flex: none; }
</style>
</head>
<body>
  <main class="sign">
    <section class="header">
      <div class="headline">
        <div class="line-one"><span class="hl-yellow">Helicopter</span> <span class="hl-blue">Joy Flights</span></div>
        <div class="line-two"><span class="hl-yellow">&amp;</span> <span class="hl-blue">Scenic Tours</span></div>
        <div class="season">here seven days from October to March</div>
      </div>
    </section>

    <svg class="price-pennant" viewBox="0 0 219 474" aria-label="Just $99 per person">
      <defs>
        <linearGradient id="pennant-fill" x1="0" y1="0" x2="0" y2="1">
          <stop offset="0" stop-color="#fff200"/>
          <stop offset="0.75" stop-color="#fff200"/>
          <stop offset="1" stop-color="#fff98a"/>
        </linearGradient>
      </defs>
      <polygon points="0,0 219,0 219,395 110,474 0,395" fill="url(#pennant-fill)"/>
      <text x="110" y="105" font-size="64">just</text>
      <text x="110" y="205" font-size="92">$99</text>
      <text x="110" y="280" font-size="64">per</text>
      <text x="110" y="355" font-size="66">person</text>
    </svg>

    <div class="photo" role="img" aria-label="Photo of a black helicopter flying low over turquoise ocean and a sandy beach with coastal dunes"></div>

    <section class="offer-band">
      <div><span class="accent">$99</span> flights are shared <span class="accent">8 MINUTE</span> flights</div>
      <div>and are only available on weekends</div>
    </section>

    <section class="footer">
      <div class="brand">
        <div class="brand-dot"></div>
        <div class="brand-name">WENDALOFT<br>HELICOPTERS</div>
      </div>
      <div class="contact">
        <div>For more details call us</div>
        <div class="row">
          <svg class="icon" viewBox="0 0 28 28" aria-hidden="true">
            <circle cx="14" cy="14" r="14" fill="#fff200"/>
            <path d="M9 7c1-.6 2-.4 2.5.5l1.3 2.4c.4.8.2 1.6-.5 2.1l-1 .7c.8 1.9 2.2 3.4 4 4.3l.8-1c.5-.6 1.4-.8 2.1-.4l2.3 1.4c.8.5 1 1.6.4 2.4l-.8 1c-.7.8-2 1.1-3 .7C12 19.4 8.6 16 7 11.5c-.4-1 0-2.3.8-3z" fill="#1b6fb5"/>
          </svg>
          <span>9372 6105</span>
        </div>
        <div class="row web">
          <svg class="icon" viewBox="0 0 28 28" aria-hidden="true">
            <circle cx="14" cy="14" r="14" fill="#fff200"/>
            <circle cx="14" cy="14" r="8" fill="#1b6fb5"/>
            <path d="M6 14h16M14 6c-3 3-3 13 0 16M14 6c3 3 3 13 0 16" stroke="#fff200" stroke-width="1.4" fill="none"/>
          </svg>
          <span>www.wendaloft.com.au</span>
        </div>
      </div>
    </section>
  </main>
</body>
</html>
```